project - Plume Den

Dear designers, I'm Looking for an appealing new business card design to represent us for our new e-cigarette store: The PlumE Den. Knowledgeable and friendly staff we aim for superior customer service with a positive atmosphere. Classic feel with modern touch is what we are aiming for . Lime green font and grey back round is the original color scheme but we are flexible and open to suggestions. I added some doodles to show you where my mind is at. address: 4826 97 St SW Edmonton, AB (inside the grand bazaar hall)web: theplumeden.com email: info@theplumeden.com phone : 780.555.6147 Thanks and am looking forward to seeing your creative , fresh and innovative designs.
Good luck everybody!
Gavin
lime green and charcoal grey please. thanks
Business
The PlumE Den

```html
<!DOCTYPE html>
<html lang="en">
<head>
<meta charset="utf-8">
<title>The PlumE Den — Business Card</title>
<link href="https://fonts.googleapis.com/css2?family=Crimson+Pro:wght@400&display=swap" rel="stylesheet">
<style>
  :root {
    --stage: #1c1c1d;
    --card: #2b2b2c;
    --card-edge: #333334;
    --lime: #b5d334;
    --lime-faint: rgba(181, 211, 52, 0.16);
    --ink-soft: #c9c9c9;
    --ink-muted: #9a9a9a;
    --rule: #8a8a8a;
    --serif: "Crimson Pro", Georgia, serif;
  }
  * { box-sizing: border-box; margin: 0; padding: 0; }
  html, body {
    width: 1200px; height: 900px; overflow: hidden;
    background: var(--stage);
    font-family: var(--serif);
  }
  .canvas {
    position: relative; width: 1200px; height: 900px;
  }
  .card {
    position: absolute; left: 325px;
    width: 550px; height: 314px;
    background: linear-gradient(160deg, var(--card-edge), var(--card) 60%);
    overflow: hidden;
    box-shadow: 0 12px 30px rgba(0,0,0,0.45);
  }
  .card--front { top: 85px; }
  .card--back { top: 475px; }

  /* Front */
  .brand {
    position: absolute; left: 0; right: 0; top: 112px;
    text-align: center;
  }
  .brand__name {
    color: var(--lime);
    font-size: 46px; letter-spacing: 0.04em;
    text-transform: uppercase; line-height: 1;
  }
  .brand__web {
    margin-top: 10px;
    color: var(--ink-soft);
    font-size: 11px; letter-spacing: 0.32em;
  }

  /* Back */
  .smoke {
    position: absolute; left: -20px; top: 40px;
    width: 260px; height: 300px;
    background: radial-gradient(ellipse at 45% 55%, rgba(220,220,220,0.22), rgba(220,220,220,0.06) 55%, transparent 75%);
  }
  .backdrop-name {
    position: absolute; left: 40px; top: 30px;
    color: var(--lime-faint);
    font-size: 58px; letter-spacing: 0.04em;
    text-transform: uppercase; line-height: 1;
    white-space: nowrap;
  }
  .address {
    position: absolute; left: 225px; top: 118px;
    line-height: 1.15;
  }
  .address__street { color: var(--lime); font-size: 17px; }
  .address__note { color: var(--ink-soft); font-size: 14px; }
  .contact {
    position: absolute; left: 210px; top: 200px;
    display: flex; gap: 10px;
  }
  .contact__labels {
    text-align: right;
    color: var(--ink-muted);
    font-size: 9.5px; letter-spacing: 0.08em;
    line-height: 17px;
    padding-top: 14px;
    padding-right: 9px;
    border-right: 1px solid var(--rule);
  }
  .contact__values {
    color: var(--lime);
    font-size: 16px; line-height: 17px;
  }
</style>
</head>
<body>
<main class="canvas">

  <section class="card card--front" aria-label="Business card front">
    <div class="brand">
      <div class="brand__name">The PlumE Den</div>
      <div class="brand__web">www.theplumeden.com</div>
    </div>
  </section>

  <section class="card card--back" aria-label="Business card back">
    <div class="smoke" role="img" aria-label="Soft white wisps of vapour swirling across the card"></div>
    <div class="backdrop-name" aria-hidden="true">The PlumE Den</div>

    <div class="address">
      <div class="address__street">4826 97 St SW Edmonton, AB</div>
      <div class="address__note">(inside the grand bazaar hall)</div>
    </div>

    <div class="contact">
      <div class="contact__labels">
        <div>PHONE</div>
        <div>EMAIL</div>
        <div>WEB</div>
      </div>
      <div class="contact__values">
        <div>780.555.6147</div>
        <div>info@theplumeden.com</div>
        <div>www.theplumeden.com</div>
      </div>
    </div>
  </section>

</main>
</body>
</html>
```